Guinea Pigs and Budgerigars Stud card design

The stud name for our animals is "Tarrimbee" We offer a service for stud cavies (guinea pigs) and offer show and pet stock for sale. We also have show and pet stock for sale for show budgerigars as well

The animals/birds we show are very beautiful and we are a very professional stud. Our property entrance is in Black so we would also like to reflect that in the card, with Tarrimbee and all writing in black. We can supply 2 photos to be integrated into the card, one of a black guinea pig and one of a yellow budgerigar. Tarrimbee also means 'place of many owls' so we would also like an owl (not a cartoon type, a natural looking owl, preferably an australian barn owl) integrated into the design as well :)
Updates

Please also add the website address to the design
http://www.tarrimbeestud-example.com

Target Market(s)

professional animal breeders and families new to the industry

Industry/Entity Type

Pet

Contact Information for Business Card

Tarrimbee
Melinda Harroway and Gavin Thorley
Quellam Creek Qld
0412 867 203

Requirements
Must have
• card to integrate 2 photos plus an owl ( I will try to find an example pic)

```html
<!DOCTYPE html>
<html lang="en">
<head>
<meta charset="utf-8">
<title>Tarrimbee – Stud Card</title>
<link rel="stylesheet" href="https://fonts.googleapis.com/css2?family=Open+Sans:wght@400;600&display=swap">
<style>
  :root {
    --panel-dark: #1c1c1c;
    --panel-mid: #5e5e5e;
    --wood-light: #e6e6e6;
    --wood-line: rgba(160,160,160,0.25);
    --title-grey: #6d6d6d;
    --leather: #7a3a17;
    --leather-dark: #4e210a;
    --stitch: #2b1306;
    --bar-top: #3a3a3a;
    --bar-bottom: #050505;
    --ink: #1e1e1e;
    --white: #ffffff;
    --owl-cream: #e9dcc4;
    --owl-brown: #8a6a48;
    --cavy-beige: #d9c6a4;
    --budgie-yellow: #f2e21c;
  }
  html, body { margin: 0; padding: 0; overflow: hidden; background: #ffffff; }
  .card {
    position: relative;
    width: 1200px;
    height: 693px;
    overflow: hidden;
    font-family: "Open Sans", Arial, sans-serif;
    background:
      repeating-linear-gradient(180deg, transparent 0 68px, var(--wood-line) 68px 70px),
      linear-gradient(90deg, #dcdcdc, var(--wood-light) 40%, #efefef);
  }
  .dark-panel {
    position: absolute; left: 0; top: 0; width: 382px; height: 693px;
    background:
      repeating-linear-gradient(180deg, transparent 0 68px, rgba(255,255,255,0.06) 68px 70px),
      linear-gradient(160deg, var(--panel-dark) 0%, #3c3c3c 45%, var(--panel-mid) 100%);
  }
  .stud-name {
    position: absolute; left: 108px; top: 28px;
    margin: 0;
    font-size: 196px; font-weight: 400; letter-spacing: -4px; line-height: 1;
    color: var(--title-grey);
    white-space: nowrap;
  }
  .tagline-tag {
    position: absolute; left: 107px; top: 294px; width: 578px; height: 132px;
    border-radius: 16px;
    background: radial-gradient(ellipse at 40% 40%, var(--leather) 0%, var(--leather-dark) 100%);
    box-shadow: 0 3px 6px rgba(0,0,0,0.4);
  }
  .tagline-tag::before {
    content: ""; position: absolute; inset: 10px;
    border: 2px dashed var(--stitch); border-radius: 10px;
  }
  .tagline {
    position: absolute; inset: 0; margin: 0;
    display: flex; flex-direction: column; justify-content: center; align-items: center;
    color: var(--white); font-size: 29px; line-height: 1.42; white-space: nowrap;
  }
  .photo { position: absolute; }
  .photo-owl {
    left: 34px; top: 457px; width: 276px; height: 236px;
    border-radius: 48% 48% 0 0;
    background: radial-gradient(ellipse at 50% 40%, var(--owl-cream) 0%, #cbb896 55%, var(--owl-brown) 100%);
  }
  .photo-cavy {
    left: 740px; top: 314px; width: 200px; height: 160px;
    border-radius: 50% 45% 40% 50%;
    background: radial-gradient(ellipse at 40% 40%, #ebdcc0 0%, var(--cavy-beige) 60%, #b59f7c 100%);
  }
  .photo-budgie {
    left: 926px; top: 170px; width: 204px; height: 327px;
    border-radius: 50% 50% 40% 40%;
    background: radial-gradient(ellipse at 50% 35%, #fff27a 0%, var(--budgie-yellow) 55%, #d3b80a 100%);
  }
  .owners-bar {
    position: absolute; left: 443px; top: 474px; width: 658px; height: 48px;
    border-radius: 12px;
    background: linear-gradient(180deg, var(--bar-top), var(--bar-bottom));
    color: var(--white); font-size: 32px; line-height: 48px; text-align: center;
    margin: 0; white-space: nowrap;
  }
  .address {
    position: absolute; left: 457px; top: 533px; margin: 0;
    font-style: normal; color: var(--ink); font-size: 25px; line-height: 38px;
    white-space: nowrap;
  }
  .owl-mark { position: absolute; left: 666px; top: 581px; width: 34px; height: 49px; }
  .online {
    position: absolute; left: 712px; top: 563px; width: 430px; margin: 0;
    text-align: center; color: var(--ink); font-size: 26px; line-height: 40px;
    white-space: nowrap;
  }
</style>
</head>
<body>
  <main class="card">
    <div class="dark-panel"></div>
    <h1 class="stud-name">Tarrimbee</h1>

    <div class="tagline-tag">
      <p class="tagline"><span>Breeders of Exhibition</span><span>Budgerigars and Pedigree Cavies</span></p>
    </div>

    <div class="photo photo-owl" role="img" aria-label="Photo of an Australian barn owl"></div>
    <div class="photo photo-cavy" role="img" aria-label="Photo of a pale guinea pig"></div>
    <div class="photo photo-budgie" role="img" aria-label="Photo of a yellow exhibition budgerigar"></div>

    <p class="owners-bar">Melinda Harroway &amp; Gavin Thorley</p>

    <address class="address">
      Quellam Creek Qld<br>
      0412 867 203<br>
      0423 551 908
    </address>

    <svg class="owl-mark" viewBox="0 0 34 49" role="img" aria-label="Small owl silhouette">
      <ellipse cx="17" cy="28" rx="14" ry="20" fill="#111"/>
    </svg>

    <p class="online">www.tarrimbeestud-example.com<br>tarrimbee@example-mail.com</p>
  </main>
</body>
</html>
```